Website Home Page Re-Design for a Media Company producing Catholic Bible studies on CD/DVD/MP3

UPDATED BRIEF AS OF 12/28/15:

I have been in touch our rep at ArtHive and we are going to extend this design starting on January 9. There were a couple of designs that came out ok -- I could do the tweaking on my end with the body and footer in psd -- but for every single layout the hero section is lacking. So, I guess the main thing that would create a winner is can you create an amazing hero section. I updated the brief once already truncating the focus of design elements -- I am truncating it again here to have you focus on just 1 design element -- who can create the best hero section. Something better has to be possible. I greatly appreciate your attention to this element.

UPDATED BRIEF AS OF 12/21/15:

Ladies and Gentlemen,

Thus far none of the submitted layouts fit the bill (issues being a combination of layouts, design elements, and a lot of samples with too many competing vibrant colors, etc.). So, I just finished putting together an updated template on my own (attached as updated-template.png). I am hoping that now that the layout and color scheme are firmed up (with the exceptions mentioned below), your more focused attention on the following elements will bring about a better result. For, now you are playing/manipulating just elements and not also an overall layout. Please use the bones of this updated template and focus your attention on the following while not adjusting anything not mentioned below:

Starting from the top down:

(1) I'm open to the top section with the logo/need assistance/cart icon/ etc. being manipulated around to make the Sign in and Create account links more noticeable whilst not looking crowded or forced. Not sure if things can go on different lines/different colors implemented, etc. -- that's for you to tinker with if you so choose. Keep the colors of the "Need Assistance" that turquoise blue and the phone and email icons that same orange.

(2) Still open to a better hero section. Found this to be the most disappointing part of the templates submitted thus far. I think rather than slapping images up there on a background that looks like a circus, if some real intricate time was put on making some of the CD's look very nice would help -- how to assemble them and incorporate the tag line is up to you.

(3) For the "Most Popular" and "New Releases" section, if something jumps out at you as far as how to layout the CD images that will populate this section better, I'm open. For instance, would a lighter gray background box work well behind the CD images? Would eliminating the thinly outlined rectangles around the cd images look better? Would assembling them not just in one row horizontally look better, etc.? Keep the titles and those horizontal lines on either sides of the category section the same -- but the layout of the cd images that will populate these sections are open to be modified. Keep in mind NOT TO CROWD THIS AREA -- some templates submitted just looked a mess with not enough white space, making it look very crammed and lacking distinct sections for the eye to be drawn to -- having the effect of "where do I look"?

(4) I need 3 well-designed iconic images for the Blog, Rewards Program, and Chatterly links in the gray rectangular box near the bottom. From top to bottom, the three icons combined (in total height) should be the height of the entire still frame that is situated to the left. Keep in mind, once again, space between them -- they should not looked crammed. FYI, the "Veriday Media Blog" logo as you see on our blog (veridaymediablog.com) should be a part of whatever icon you end up using.

Thank you.

INITIAL BRIEF:

1 PAGE ONLY
I am looking for a re-design of our home page at store.veridaymedia.com -- you can see our current layout there. Our e-commerce store is hosted on ShopLoom.com.

I am uploading a screen shot here of what CONTENT I would like to see on our home page, but obviously it needs to be laid out with a much more professional and polished look to -- not using the layout I currently have -- want someone who really knows what they're doing to create a really polished presentation of the CONTENT. Please pay close attention to the following considerations:

(1) As far as colors, it needs to flow well with the other pages of the website, as those will not be changes (i.e., the category pages and the product pages).

(2) I've laid out the elements in the attached design in somewhat order of importance:

(A) Visitors should see the Catch title of "Grasp the Scriptures As Never Until Now" (though this is subject to modify -- wording may be different) at the top somewhere as an eye catcher (would probably be wise to have some type of graphic like our cd covers as I have them in the screen shot, but this is definitely where your artistic talents of placement and manipulation if graphics must take over). I like the look of the cd sets in the top banner in the attached screen shot inasmuch as they look like they're stepping out of the rectangle/hero section-- obviously you can use whatever image(s) you deem appropriate and can include or exclude this design aspect -- just throwing that out there, but don't think it's mandatory if it doesn't work with the overall design.

(B) Then our most popular Bible studies section which will be populated by automated settings on the back end of shoploom.

(C) Then our Join our email list option

(C.i.) I don't have it in the attached screen shot but we MIGHT end up doing a "Who Are We Video?" I do not know if it is possible to create the page layout such that there is room to add the image of the video still frame at some point in the future. If not just assume no video at this point.

(D) The Latest Releases is beneath the join our email list section merely because I thought there needed to be a break between having two rows of CD's merely differentiated by the title of each row (Most Popular Bible Studies vs. Latest Releases).

(E) Next is something graphically eye catching for our Blog, Chatterly and Rewards Program. Again, I just threw those images together -- not very polished or, in my estimation, very attractive -- your abilities must reign here again.

(F) Then there are what I'd call "secondary" links in the bottom horizontal black bar in the attached screen shot that are currently right beneath the bottom black bar on our current store page (e.g., Home, Services, About Us and so on). Those should be present, but obviously can be laid out in whatever design layout you envision.

(G) The Safeknot, Payment Options, and "All Prices..." need to be present at the bottom too.

(H) Just noticed this -- the Search Bar obviously needs to be present as well in a noticeable way near the "Primary" links.

Again, these are just in order of importance for the most part -- they don't have to go in a perfectly lined up vertical order from top to bottom, but the eye should be drawn to the elements in roughly that order.

(2) We are looking for a clean, "elegant" home page that incorporates the elements in the attached screen shot mentioned above and doesn't look cluttered or busy.

I like the black gradient of the horizontal bars across the top and bottom in conjunction with the flesh-like gradient color of the top rectangle box/hero image -- that contrast, along with a good bit of white space works well, though I'm certainly not opposed to other color schemes -- but it has to be consonant with the other category and product pages on the website pages -- if you re-create the top section and bottom section such that the other category and product pages top and bottom sections need to be modified, that is fine if it means a much better designed home page. Not looking for a super tall page either, but it obviously will need to be taller than it currently stands at store.veridaymedia.com given what we're adding to it.

(3) I don't know if there is a way to make the "Sign In" and "Create Account" more prominent at the top (or elsewhere in the design) - different fonts or fonts + icons, etc.? I think, most probably, Sign in and Create Account need to go first when read from left to right if it stayed in its current position. But, having said that, I'm not opposed to modifying the entire top section either (where our logo and the cart button currently is) if that works better with a winning design.

(4) Obviously we are eliminating the carousel of images -- only one "hero" image.

(5) Any Fonts should be clean and easy to read.

Other comments about our company:

(6) Our target audience is 25-80 year old people (yes, a broad spectrum, but I can at least say our primary audience is not teenage).

(7) Our company is dedicated to providing Catholic Bible studies on CD, DVD, and MP3.

(8) The reason why we are trying to change up the design is to try to make it more explicit what we have to offer in the first 5 seconds for those who land on our home page and do not know much about us. Trying to make it very focused on the products we offer with more image/iconic based sections of content -- e.g., as opposed to just having the text link for cd's, the blog, or the join our email list in the bottom black horizontal bar, we are dedicating a small iconic section to each of those categories.

Requirements
Must have
• Attached is our logo in a png format with both white background and transparent as well as in black and white and in color. You can use the text "Veriday Media" in the logo as found in the png's attached below or shifted over to the right as found at Store.veridaymedia.com.
Nice to have
• I've attached some layouts here that I like -- obviously would want some distinct layouts, but this hopefully relays the design-type, keeping in mind the comments I've made above in the project description.

```html
<!DOCTYPE html>
<html lang="en">
<head>
<meta charset="utf-8">
<title>Veriday Media — Home</title>
<link href="https://fonts.googleapis.com/css2?family=Arimo:wght@400;700&family=Gelasio:wght@400&display=swap" rel="stylesheet">
<style>
  :root {
    --ink: #1a1a1a;
    --text: #222;
    --muted: #555;
    --accent-blue: #19aee0;
    --accent-orange: #e8912d;
    --rule: #8a8a8a;
    --paper: #ffffff;
    --band: #f3f2ee;
    --field-border: #9a9a9a;
    --placeholder: #8a8a8a;
    --button: #6b6b6b;
    --hero-text: #ffffff;
  }
  * { box-sizing: border-box; margin: 0; padding: 0; }
  html, body { width: 1200px; height: 975px; overflow: hidden; background: var(--paper); }
  body { position: relative; font-family: "Arimo", Arial, sans-serif; color: var(--text); }

  .site-header { position: absolute; top: 0; left: 0; width: 1200px; height: 180px; }
  .brand { position: absolute; left: 68px; top: 38px; display: flex; align-items: center; gap: 14px; }
  .brand-mark { width: 54px; height: 44px; background: var(--ink); }
  .brand-name { font-family: "Arimo", Arial, sans-serif; font-weight: 700; font-size: 29px; line-height: 30px; letter-spacing: 1px; color: var(--ink); text-transform: uppercase; }

  .utility { position: absolute; top: 25px; right: 67px; display: flex; align-items: center; font-size: 12px; }
  .utility .help { color: var(--accent-blue); margin-right: 25px; }
  .utility .contact { display: flex; align-items: center; gap: 7px; font-weight: 700; color: var(--text); margin-left: 24px; }
  .utility .contact:first-of-type { margin-left: 0; }

  .account { position: absolute; top: 61px; right: 67px; display: flex; align-items: center; font-size: 14px; gap: 17px; }
  .account .cart { display: flex; align-items: center; gap: 6px; }

  .search { position: absolute; top: 101px; left: 965px; width: 168px; height: 24px; border: 1px solid var(--ink); display: flex; align-items: center; justify-content: space-between; padding: 0 7px; font-size: 14px; color: var(--text); }

  .header-rule { position: absolute; top: 141px; left: 49px; width: 1102px; height: 2px; background: var(--rule); }

  .main-nav { position: absolute; top: 152px; left: 67px; right: 67px; display: flex; justify-content: space-between; font-size: 15px; color: var(--text); }
  .main-nav .has-menu::after { content: ""; display: inline-block; margin-left: 5px; vertical-align: middle; border-left: 4px solid transparent; border-right: 4px solid transparent; border-top: 5px solid var(--text); }

  .hero { position: absolute; top: 180px; left: 0; width: 1200px; height: 497px; }
  .hero-photo { position: absolute; inset: 0;
    background:
      linear-gradient(160deg, rgba(20,10,4,0.9) 0%, rgba(20,10,4,0) 28%),
      linear-gradient(115deg, #a3622c 0%, #c98a4a 22%, #3a2312 34%, #c07a3a 46%, #8f5224 62%, #2a170a 78%, #6a3a18 100%); }
  .hero-copy { position: absolute; top: 91px; left: 578px; width: 600px; text-align: center; color: var(--hero-text); font-family: "Gelasio", Georgia, serif; }
  .hero-copy h1 { font-weight: 400; font-size: 50px; line-height: 60px; }
  .hero-copy p { margin-top: 20px; font-size: 24px; line-height: 36px; }

  .newsletter { position: absolute; top: 677px; left: 0; width: 1200px; height: 298px; background: var(--band); font-family: "Gelasio", Georgia, serif; }
  .newsletter-intro { position: absolute; top: 58px; left: 118px; width: 500px; text-align: center; color: var(--muted); }
  .newsletter-intro h2 { font-weight: 400; font-size: 37px; line-height: 48px; }
  .newsletter-intro p { margin-top: 12px; font-size: 23px; line-height: 36px; }
  .newsletter-form { position: absolute; top: 66px; left: 704px; width: 345px; }
  .field { height: 42px; border: 1px solid var(--field-border); background: var(--paper); padding: 0 13px; display: flex; align-items: center; font-size: 17px; color: var(--placeholder); margin-bottom: 24px; }
  .field + .field { height: 40px; }
  .join { width: 120px; height: 36px; background: var(--button); color: #fff; border-radius: 2px; display: flex; align-items: center; justify-content: center; font-size: 18px; }
</style>
</head>
<body>
  <header class="site-header">
    <div class="brand">
      <span class="brand-mark"></span>
      <span class="brand-name">Veriday<br>Media</span>
    </div>

    <div class="utility">
      <span class="help">Need Assistance?</span>
      <span class="contact">
        <svg width="16" height="16" viewBox="0 0 16 16" aria-hidden="true"><circle cx="8" cy="8" r="7" fill="none" stroke="var(--accent-orange)" stroke-width="1.4"/><path d="M5.5 4.5l1.4-.3.8 1.8-.9.7c.4 1 1.1 1.7 2.1 2.1l.7-.9 1.8.8-.3 1.4c-3 .1-5.7-2.6-5.6-5.6z" fill="var(--accent-orange)"/></svg>
        (555) 214-0873
      </span>
      <span class="contact">
        <svg width="16" height="16" viewBox="0 0 16 16" aria-hidden="true"><circle cx="8" cy="8" r="7.5" fill="var(--accent-orange)"/><rect x="4.5" y="5.5" width="7" height="5" fill="#fff"/><path d="M4.5 5.5l3.5 2.7 3.5-2.7" fill="none" stroke="var(--accent-orange)" stroke-width="0.9"/></svg>
        Email Us
      </span>
    </div>

    <nav class="account">
      <span>Sign In</span>
      <span>Create Account</span>
      <span class="cart">Cart
        <svg width="22" height="16" viewBox="0 0 22 16" aria-hidden="true"><path d="M0 1h4l3 9h11l3-7H6" fill="none" stroke="var(--ink)" stroke-width="1.8"/><path d="M7 4h13l-2.5 5H8.5z" fill="var(--ink)"/><circle cx="9" cy="13.5" r="1.6" fill="var(--ink)"/><circle cx="16" cy="13.5" r="1.6" fill="var(--ink)"/></svg>
      </span>
    </nav>

    <div class="search">
      <span>Search</span>
      <svg width="14" height="14" viewBox="0 0 14 14" aria-hidden="true"><circle cx="5.5" cy="5.5" r="4.2" fill="none" stroke="var(--ink)" stroke-width="1.8"/><path d="M8.6 8.6l4.4 4.4" stroke="var(--ink)" stroke-width="2.2"/></svg>
    </div>

    <div class="header-rule"></div>

    <nav class="main-nav">
      <span class="has-menu">Speaker</span>
      <span>CD</span>
      <span>DVD</span>
      <span>MP3</span>
      <span>Class</span>
      <span>Book</span>
      <span>Conference</span>
      <span class="has-menu">Category</span>
      <span>Blog</span>
      <span>Rewards Program</span>
      <span>Gift Certificates</span>
      <span>Wishlist</span>
    </nav>
  </header>

  <section class="hero">
    <div class="hero-photo" role="img" aria-label="Photo of a Bible study book lying on a sunlit wooden table beside a dark chair, with window shadows across the wood"></div>
    <div class="hero-copy">
      <h1>Grasp the Scriptures<br>As Never Until Now</h1>
      <p>With our wide selection of<br>Biblical study recordings and books</p>
    </div>
  </section>

  <section class="newsletter">
    <div class="newsletter-intro">
      <h2>Subscribe to our newsletter</h2>
      <p>Join over 10000 members<br>and get a free Daniel Hartwell MP3</p>
    </div>
    <div class="newsletter-form">
      <div class="field">Your First Name</div>
      <div class="field">Your Email Address</div>
      <div class="join">Join</div>
    </div>
  </section>
</body>
</html>
```